Store Promo Card (already have logo!)

I need a card design (single side) for my online women’s gift shop containing a promotional code to be placed in bags for attendees at an event. I’m flexible on both shape and sizing, but perhaps a 4x6 card.
—It should contain my attached logo, my website (www.corvidtpq.com), and my Instagram handle (@corvidtpq) and promotion language such as “15% off your purchase with code: MIRVOL”.
—I think I would like my logo to be large.
—It should be clean, simple and modern in design and should use the colors from my logo.
—I would like about 3-5 product pictures depending on design.
Target Market(s)
Women ages 30 to 60
Industry/Entity Type
Retail Upscale Gift
Look and feel

```html
<!DOCTYPE html>
<html lang="en">
<head>
<meta charset="utf-8">
<title>Corvid Promo Card</title>
<link rel="stylesheet" href="https://fonts.googleapis.com/css2?family=Abril+Fatface&family=Cinzel:wght@600&family=Montserrat:wght@600&display=swap">
<style>
  :root {
    --backdrop: #30313c;
    --blush: #efcdc5;
    --slate: #6a6a6a;
    --ink: #595c5b;
    --paper: #ffffff;
  }
  html, body {
    margin: 0;
    padding: 0;
    width: 1200px;
    height: 1025px;
    overflow: hidden;
    background: var(--backdrop);
  }
  .promo-card {
    position: absolute;
    left: 100px;
    top: 202px;
    width: 1000px;
    height: 620px;
    background: var(--slate);
  }
  .card-frame {
    position: absolute;
    inset: 0;
  }
  .card-panel {
    position: absolute;
    left: 55px;
    top: 55px;
    width: 890px;
    height: 445px;
    background: var(--paper);
  }
  .brand-name {
    position: absolute;
    top: 40px;
    left: 0;
    right: 0;
    margin: 0;
    text-align: center;
    font-family: "Abril Fatface", serif;
    font-weight: 400;
    font-size: 118px;
    line-height: 1;
    letter-spacing: 2px;
    color: var(--ink);
  }
  .offer-line {
    position: absolute;
    top: 210px;
    left: 0;
    right: 0;
    margin: 0;
    text-align: center;
    font-family: "Cinzel", serif;
    font-weight: 600;
    font-size: 40px;
    letter-spacing: 3px;
    color: var(--ink);
  }
  .promo-code {
    position: absolute;
    top: 285px;
    left: 50%;
    transform: translateX(-50%);
    width: 290px;
    height: 84px;
    background: var(--blush);
    display: flex;
    align-items: center;
    justify-content: center;
  }
  .promo-code::before {
    content: "";
    position: absolute;
    inset: 8px;
    border: 1.5px dashed var(--ink);
  }
  .promo-code span {
    font-family: "Cinzel", serif;
    font-weight: 600;
    font-size: 40px;
    letter-spacing: 4px;
    color: var(--ink);
  }
  .gift-icon {
    position: absolute;
    left: 38px;
    top: 280px;
    width: 130px;
    height: 150px;
  }
  .contact-row {
    position: absolute;
    left: 360px;
    top: 538px;
    display: flex;
    gap: 46px;
    align-items: center;
  }
  .contact-item {
    display: flex;
    align-items: center;
    gap: 12px;
    font-family: "Montserrat", sans-serif;
    font-weight: 600;
    font-size: 22px;
    letter-spacing: 1.5px;
    color: var(--paper);
  }
  .contact-item svg {
    width: 40px;
    height: 40px;
  }
</style>
</head>
<body>
  <div class="promo-card">
    <svg class="card-frame" width="1000" height="620" viewBox="0 0 1000 620" aria-hidden="true">
      <polygon points="0,0 1000,0 945,55 55,55 55,500 0,560" fill="var(--blush)"/>
    </svg>

    <div class="card-panel">
      <h1 class="brand-name">CORVID</h1>
      <p class="offer-line">15% OFF YOUR PURCHASE</p>
      <div class="promo-code"><span>MIRVOL</span></div>

      <svg class="gift-icon" viewBox="0 0 130 150" fill="none" stroke="var(--ink)" stroke-width="7" stroke-linejoin="round" aria-hidden="true">
        <rect x="12" y="78" width="92" height="66"/>
        <line x1="58" y1="78" x2="58" y2="144"/>
        <polygon points="8,40 112,22 118,52 14,70"/>
        <line x1="60" y1="31" x2="66" y2="61"/>
        <path d="M60 31 C40 10 30 25 45 33 Z"/>
        <path d="M60 31 C70 5 85 18 72 28 Z"/>
      </svg>
    </div>

    <div class="contact-row">
      <div class="contact-item">
        <svg viewBox="0 0 40 40" aria-hidden="true">
          <circle cx="20" cy="20" r="18" fill="var(--paper)"/>
        </svg>
        <span>@corvidtpq</span>
      </div>
      <div class="contact-item">
        <svg viewBox="0 0 40 40" aria-hidden="true">
          <circle cx="20" cy="20" r="18" fill="var(--paper)"/>
          <g fill="none" stroke="var(--slate)" stroke-width="2">
            <circle cx="20" cy="20" r="10"/>
            <ellipse cx="20" cy="20" rx="4.5" ry="10"/>
            <line x1="10" y1="20" x2="30" y2="20"/>
          </g>
        </svg>
        <span>www.corvidtpq.com</span>
      </div>
    </div>
  </div>
</body>
</html>
```